Trellmark Vista brochure

A brochure based on the word document provided. Brochure provided in Word and PDF format. Should include pictures and shorten to make it a brochure of no more than two 8.5x11 pages. Completed brochure file must be under 5 megabytes.

Leadership

• final file size less than 5 megabytes. also file in Word and PDF and any other that makes sense. Must have pictures or graphics to support the text. Include the 3 logos attached from TKR, qoVantra, and Trellmark vista. qoVantra logo is in attachments you can get logo for Trellmark Vista at www.trellmarkvista.com. or http://www.trellmarkvista.com/images/logo.png

```html
<!DOCTYPE html>
<html lang="en">
<head>
<meta charset="utf-8">
<title>Trellmark Vista Brochure – Revision 02</title>
<link rel="stylesheet" href="https://fonts.googleapis.com/css2?family=Open+Sans:wght@700;800&family=Arimo:wght@400&display=swap">
<style>
  :root {
    --bg: #ececec;
    --paper: #ffffff;
    --orange: #ee6b2e;
    --blue: #1d95c8;
    --ink: #2a2a2a;
    --title: #111111;
  }
  * { margin: 0; padding: 0; box-sizing: border-box; }
  html, body { width: 1200px; height: 508px; overflow: hidden; background: var(--bg); }
  .sheet { position: relative; width: 1200px; height: 508px; }
  .sheet-title {
    position: absolute; top: 20px; left: 0; width: 1200px; text-align: center;
    padding-right: 96px;
    font: 700 44px/1 "Open Sans", sans-serif; color: var(--title); letter-spacing: 1px;
  }
  .option { position: absolute; top: 88px; width: 268px; }
  .option-1 { left: 22px; }
  .option-2 { left: 314px; }
  .option-3 { left: 608px; }
  .option-4 { left: 900px; }
  .page {
    position: relative; width: 268px; height: 348px; background: var(--paper);
    box-shadow: 2px 3px 6px rgba(0,0,0,.35); overflow: hidden;
  }
  .page-art { position: absolute; top: 0; left: 0; width: 268px; height: 348px; }
  .copy {
    position: absolute; top: 128px; left: 10px; width: 248px;
    font: 400 4.7px/5.8px "Arimo", sans-serif; color: var(--ink); text-align: justify;
  }
  .copy p { margin-bottom: 1.6px; }
  .copy ul { list-style: none; margin: 0 0 1.6px 14px; }
  .copy li { position: relative; margin-bottom: 1.4px; padding-right: 20px; text-align: left; }
  .copy li::before {
    content: ""; position: absolute; left: -6px; top: 1.9px; width: 2px; height: 2px;
    border-radius: 50%; background: var(--orange);
  }
  .option-label {
    margin-top: 14px; text-align: center;
    font: 700 23px/1 "Open Sans", sans-serif; color: var(--title); letter-spacing: .5px;
  }
</style>
</head>
<body>
<div class="sheet">
  <h1 class="sheet-title">REVISION 02</h1>

  <section class="option option-1">
    <div class="page">
      <svg class="page-art" viewBox="0 0 268 348">
        <defs>
          <linearGradient id="sky-stairs" x1="0" y1="0" x2="0" y2="1">
            <stop offset="0" stop-color="#9cc4e4"/>
            <stop offset=".6" stop-color="#dfeaf3"/>
            <stop offset="1" stop-color="#8f9aa6"/>
          </linearGradient>
        </defs>
        <rect width="268" height="112" fill="var(--orange)"/>
        <ellipse cx="140" cy="-10" rx="150" ry="122" fill="var(--paper)" stroke="var(--blue)" stroke-width="8"/>
        <circle cx="205" cy="255" r="78" fill="none" stroke="var(--blue)" stroke-width="34" opacity=".08"/>
        <circle cx="150" cy="215" r="40" fill="none" stroke="var(--orange)" stroke-width="18" opacity=".07"/>
        <ellipse role="img" aria-label="Photo of a businessman with a briefcase climbing stone steps into a bright sky above a city" cx="135" cy="0" rx="112" ry="104" fill="url(#sky-stairs)"/>
      </svg>
      <div class="copy">
        <p>Manager and team membership includes all the benefits of individual members for the manager and all employees. In addition, the manager receives the following:</p>
        <ul>
          <li>Manager level reports for all energy pulses; this includes aggregated data for all questions (other than personal diary items), on-line reporting, benchmark data and access to coaching calls and webinars for members only.</li>
          <li>Associate membership of the Institute for Adaptive Workplaces (TKR) at the Halvorsen School of Business, University of Westbrook. This membership comes with a badge designation level of accomplishment.</li>
          <li>As a manager associate, you will be invited to TKR webinars and other learning events (executive education programs, leadership summits, local meetings and more).</li>
          <li>You also will have access to the manager associate network of members.</li>
        </ul>
        <p>Energy Pulsing (for individual and manager associate members) – Short, energy pulses will be sent out to the entire Trellmark Vista population every other month. The pulses will include 3 core questions to assess employee energy at work; in addition, other questions will focus on key business challenges identified by the research team at TKR and also by members. The data provided to individuals and managers are different from other sources of information in that the information is:</p>
        <ul>
          <li>Trend data vs. point-in-time data; we teach managers about recovery techniques because data will fluctuate.</li>
          <li>Energy data – energy predicts performance, so tracking energy will help you improve your own work and team’s performance. We teach you how to optimize and direct energy to be at your best and achieve goals.</li>
          <li>Topics important to drive high quality dialogue and learning – In the past we have studied confidence, entrepreneurial action and idea generation, business drivers, quality and more.</li>
          <li>As a member you will have input in the questions used; we ask what questions you think are important, and we include questions that are noted by multiple participants.</li>
          <li>Your data will include benchmarks on the overall sample, industry, firm size, amount of change the company is going through (this metric is an important benchmark demographic) and more.</li>
          <li>You will receive articles, press releases and technical reports on the overall learning.</li>
        </ul>
        <p>Feedback, webinars and coaching conversations for manager associates – After each pulse, you will immediately receive your own personal reports and then when the data are aggregated (benchmarking available), you will receive your team and benchmark reports. In addition to all of the benefits of individual membership, you will be invited to webinars and coaching calls for manager associates only. In these more focused conversations, you can learn from the researchers at TKR, and also you can dialogue with peers who are facing similar challenges or opportunities.</p>
      </div>
    </div>
    <p class="option-label">OPTION 01</p>
  </section>

  <section class="option option-2">
    <div class="page">
      <svg class="page-art" viewBox="0 0 268 348">
        <defs>
          <radialGradient id="tunnel-light" cx=".5" cy=".6" r=".6">
            <stop offset="0" stop-color="#ffffff"/>
            <stop offset=".25" stop-color="#b9c2cc"/>
            <stop offset=".6" stop-color="#3a3f46"/>
            <stop offset="1" stop-color="#0d0f12"/>
          </radialGradient>
        </defs>
        <rect width="268" height="112" fill="var(--orange)"/>
        <ellipse cx="140" cy="-10" rx="150" ry="122" fill="var(--paper)" stroke="var(--blue)" stroke-width="8"/>
        <circle cx="205" cy="255" r="78" fill="none" stroke="var(--blue)" stroke-width="34" opacity=".08"/>
        <circle cx="150" cy="215" r="40" fill="none" stroke="var(--orange)" stroke-width="18" opacity=".07"/>
        <ellipse role="img" aria-label="Photo of a lone figure standing at the end of a path facing a bright light in a dark tunnel" cx="135" cy="0" rx="112" ry="104" fill="url(#tunnel-light)"/>
      </svg>
      <div class="copy">
        <p>Manager and team membership includes all the benefits of individual members for the manager and all employees. In addition, the manager receives the following:</p>
        <ul>
          <li>Manager level reports for all energy pulses; this includes aggregated data for all questions (other than personal diary items), on-line reporting, benchmark data and access to coaching calls and webinars for members only.</li>
          <li>Associate membership of the Institute for Adaptive Workplaces (TKR) at the Halvorsen School of Business, University of Westbrook. This membership comes with a badge designation level of accomplishment.</li>
          <li>As a manager associate, you will be invited to TKR webinars and other learning events (executive education programs, leadership summits, local meetings and more).</li>
          <li>You also will have access to the manager associate network of members.</li>
        </ul>
        <p>Energy Pulsing (for individual and manager associate members) – Short, energy pulses will be sent out to the entire Trellmark Vista population every other month. The pulses will include 3 core questions to assess employee energy at work; in addition, other questions will focus on key business challenges identified by the research team at TKR and also by members. The data provided to individuals and managers are different from other sources of information in that the information is:</p>
        <ul>
          <li>Trend data vs. point-in-time data; we teach managers about recovery techniques because data will fluctuate.</li>
          <li>Energy data – energy predicts performance, so tracking energy will help you improve your own work and team’s performance. We teach you how to optimize and direct energy to be at your best and achieve goals.</li>
          <li>Topics important to drive high quality dialogue and learning – In the past we have studied confidence, entrepreneurial action and idea generation, business drivers, quality and more.</li>
          <li>As a member you will have input in the questions used; we ask what questions you think are important, and we include questions that are noted by multiple participants.</li>
          <li>Your data will include benchmarks on the overall sample, industry, firm size, amount of change the company is going through (this metric is an important benchmark demographic) and more.</li>
          <li>You will receive articles, press releases and technical reports on the overall learning.</li>
        </ul>
        <p>Feedback, webinars and coaching conversations for manager associates – After each pulse, you will immediately receive your own personal reports and then when the data are aggregated (benchmarking available), you will receive your team and benchmark reports. In addition to all of the benefits of individual membership, you will be invited to webinars and coaching calls for manager associates only. In these more focused conversations, you can learn from the researchers at TKR, and also you can dialogue with peers who are facing similar challenges or opportunities.</p>
      </div>
    </div>
    <p class="option-label">OPTION 02</p>
  </section>

  <section class="option option-3">
    <div class="page">
      <svg class="page-art" viewBox="0 0 268 348">
        <defs>
          <linearGradient id="wordcloud-city" x1="0" y1="0" x2="0" y2="1">
            <stop offset="0" stop-color="#f4f6f8"/>
            <stop offset=".45" stop-color="#9fb6cc"/>
            <stop offset="1" stop-color="#2f5f8f"/>
          </linearGradient>
        </defs>
        <rect width="268" height="112" fill="var(--orange)"/>
        <ellipse cx="140" cy="-10" rx="150" ry="122" fill="var(--paper)" stroke="var(--blue)" stroke-width="8"/>
        <circle cx="205" cy="255" r="78" fill="none" stroke="var(--blue)" stroke-width="34" opacity=".08"/>
        <circle cx="150" cy="215" r="40" fill="none" stroke="var(--orange)" stroke-width="18" opacity=".07"/>
        <ellipse role="img" aria-label="Illustration of a figure silhouette built from the words success, development, knowledge, learning, training and coaching over a city skyline" cx="135" cy="0" rx="112" ry="104" fill="url(#wordcloud-city)"/>
      </svg>
      <div class="copy">
        <p>Manager and team membership includes all the benefits of individual members for the manager and all employees. In addition, the manager receives the following:</p>
        <ul>
          <li>Manager level reports for all energy pulses; this includes aggregated data for all questions (other than personal diary items), on-line reporting, benchmark data and access to coaching calls and webinars for members only.</li>
          <li>Associate membership of the Institute for Adaptive Workplaces (TKR) at the Halvorsen School of Business, University of Westbrook. This membership comes with a badge designation level of accomplishment.</li>
          <li>As a manager associate, you will be invited to TKR webinars and other learning events (executive education programs, leadership summits, local meetings and more).</li>
          <li>You also will have access to the manager associate network of members.</li>
        </ul>
        <p>Energy Pulsing (for individual and manager associate members) – Short, energy pulses will be sent out to the entire Trellmark Vista population every other month. The pulses will include 3 core questions to assess employee energy at work; in addition, other questions will focus on key business challenges identified by the research team at TKR and also by members. The data provided to individuals and managers are different from other sources of information in that the information is:</p>
        <ul>
          <li>Trend data vs. point-in-time data; we teach managers about recovery techniques because data will fluctuate.</li>
          <li>Energy data – energy predicts performance, so tracking energy will help you improve your own work and team’s performance. We teach you how to optimize and direct energy to be at your best and achieve goals.</li>
          <li>Topics important to drive high quality dialogue and learning – In the past we have studied confidence, entrepreneurial action and idea generation, business drivers, quality and more.</li>
          <li>As a member you will have input in the questions used; we ask what questions you think are important, and we include questions that are noted by multiple participants.</li>
          <li>Your data will include benchmarks on the overall sample, industry, firm size, amount of change the company is going through (this metric is an important benchmark demographic) and more.</li>
          <li>You will receive articles, press releases and technical reports on the overall learning.</li>
        </ul>
        <p>Feedback, webinars and coaching conversations for manager associates – After each pulse, you will immediately receive your own personal reports and then when the data are aggregated (benchmarking available), you will receive your team and benchmark reports. In addition to all of the benefits of individual membership, you will be invited to webinars and coaching calls for manager associates only. In these more focused conversations, you can learn from the researchers at TKR, and also you can dialogue with peers who are facing similar challenges or opportunities.</p>
      </div>
    </div>
    <p class="option-label">OPTION 03</p>
  </section>

  <section class="option option-4">
    <div class="page">
      <svg class="page-art" viewBox="0 0 268 348">
        <defs>
          <linearGradient id="ladder-wall" x1="0" y1="0" x2="1" y2="0">
            <stop offset="0" stop-color="#fbfbfb"/>
            <stop offset=".6" stop-color="#e6e8ea"/>
            <stop offset="1" stop-color="#c3c8cd"/>
          </linearGradient>
        </defs>
        <rect width="268" height="112" fill="var(--orange)"/>
        <ellipse cx="140" cy="-10" rx="150" ry="122" fill="var(--paper)" stroke="var(--blue)" stroke-width="8"/>
        <circle cx="205" cy="255" r="78" fill="none" stroke="var(--blue)" stroke-width="34" opacity=".08"/>
        <circle cx="150" cy="215" r="40" fill="none" stroke="var(--orange)" stroke-width="18" opacity=".07"/>
        <ellipse role="img" aria-label="3D illustration of a white figure holding a briefcase beside a ladder leaning on a tall brick wall" cx="135" cy="0" rx="112" ry="104" fill="url(#ladder-wall)"/>
      </svg>
      <div class="copy">
        <p>Manager and team membership includes all the benefits of individual members for the manager and all employees. In addition, the manager receives the following:</p>
        <ul>
          <li>Manager level reports for all energy pulses; this includes aggregated data for all questions (other than personal diary items), on-line reporting, benchmark data and access to coaching calls and webinars for members only.</li>
          <li>Associate membership of the Institute for Adaptive Workplaces (TKR) at the Halvorsen School of Business, University of Westbrook. This membership comes with a badge designation level of accomplishment.</li>
          <li>As a manager associate, you will be invited to TKR webinars and other learning events (executive education programs, leadership summits, local meetings and more).</li>
          <li>You also will have access to the manager associate network of members.</li>
        </ul>
        <p>Energy Pulsing (for individual and manager associate members) – Short, energy pulses will be sent out to the entire Trellmark Vista population every other month. The pulses will include 3 core questions to assess employee energy at work; in addition, other questions will focus on key business challenges identified by the research team at TKR and also by members. The data provided to individuals and managers are different from other sources of information in that the information is:</p>
        <ul>
          <li>Trend data vs. point-in-time data; we teach managers about recovery techniques because data will fluctuate.</li>
          <li>Energy data – energy predicts performance, so tracking energy will help you improve your own work and team’s performance. We teach you how to optimize and direct energy to be at your best and achieve goals.</li>
          <li>Topics important to drive high quality dialogue and learning – In the past we have studied confidence, entrepreneurial action and idea generation, business drivers, quality and more.</li>
          <li>As a member you will have input in the questions used; we ask what questions you think are important, and we include questions that are noted by multiple participants.</li>
          <li>Your data will include benchmarks on the overall sample, industry, firm size, amount of change the company is going through (this metric is an important benchmark demographic) and more.</li>
          <li>You will receive articles, press releases and technical reports on the overall learning.</li>
        </ul>
        <p>Feedback, webinars and coaching conversations for manager associates – After each pulse, you will immediately receive your own personal reports and then when the data are aggregated (benchmarking available), you will receive your team and benchmark reports. In addition to all of the benefits of individual membership, you will be invited to webinars and coaching calls for manager associates only. In these more focused conversations, you can learn from the researchers at TKR, and also you can dialogue with peers who are facing similar challenges or opportunities.</p>
      </div>
    </div>
    <p class="option-label">OPTION 04</p>
  </section>
</div>
</body>
</html>
```